Data Visualization (graphs, tables, models, circles)

We need an intuitive - user friendly - and fresh design line for our data visualization.

You know. Keep The Path Clear!

Our core product is based on the presentation and interpretation of different data sources that we combine into graphs, tables, charts etc and make visible to clients through a web platform and or Reports. Our business area is Search & Social Media Intelligence.

See Trevla.com for some inspiration in terms of current colors and a better understanding of the company. Our Logo / Name is the only one thing that cannot be changed. Everything else is up to you. Feel free to ask questions.

I have attached a few screenshots of some of our features and as you can see - there has never been a designer on this assignment. We are looking for a long term relationship with a designer that can work with us on an ongoing basis.

Design of graphs/models/circles/tables needs to be able to fit into Infographics also.

We are basically looking for an identity for our data visualization. Meaning that readers / target audience can recognize our graphs and say: Check out the cool graphs by Trevla :-)

Think: Zorbix, PlumLedger, etc. in terms of data presentation.
Updates

Project Deadline Extended
Reason: Due to illness we lost a few days last week and have not have sufficient time to look through the different designs.

Target Market(s)

Marketing People, CEO's, Strategic Planners, Ad Agencies, Decision Makers

Industry/Entity Type

Business

Requirements
Must have
• Must present at least 1 line graph (like file 1 and 2), 1 pie chart, 1 column graph and 1 matrix (like file3).

```html
<!DOCTYPE html>
<html lang="en">
<head>
<meta charset="utf-8">
<title>SEO Battle Card - Actual Competitor Matrix</title>
<link href="https://fonts.googleapis.com/css2?family=Nunito+Sans:wght@300;400&display=swap" rel="stylesheet">
<style>
  :root {
    --bg: #eeeff1;
    --brand-red: #c8102e;
    --rule-red: #e08a8f;
    --axis: #6a6a6a;
    --grid: #a5a5a8;
    --label: #77787b;
    --site-1: #d24a3f;
    --site-2: #d45547;
    --site-3: #d65b4d;
    --site-4: #dc7567;
    --site-5: #e1917f;
    --site-6: #e7ab9d;
    --site-7: #ebc3b7;
  }
  html, body {
    margin: 0;
    padding: 0;
    width: 1200px;
    height: 984px;
    overflow: hidden;
    background: var(--bg);
  }
  .battle-card {
    position: relative;
    width: 1200px;
    height: 984px;
    font-family: "Nunito Sans", Arial, sans-serif;
    color: var(--label);
  }
  .card-title {
    position: absolute;
    left: 79px;
    top: 86px;
    margin: 0;
    font-size: 26px;
    font-weight: 300;
    color: var(--brand-red);
    letter-spacing: 0.1px;
  }
  .card-rule {
    position: absolute;
    left: 79px;
    width: 968px;
    height: 1px;
    background: var(--rule-red);
  }
  .card-rule--top { top: 132px; }
  .card-rule--bottom { top: 881px; }
  .card-footer {
    position: absolute;
    left: 79px;
    top: 896px;
    margin: 0;
    font-size: 13px;
    color: var(--brand-red);
  }
  .matrix {
    position: absolute;
    left: 0;
    top: 0;
  }
  .axis-label, .tick-label, .legend-title {
    font-family: "Nunito Sans", Arial, sans-serif;
    fill: var(--label);
  }
  .axis-label { font-size: 14px; }
  .tick-label { font-size: 14px; }
  .legend-title { font-size: 12px; }
  .own-site-label {
    font-family: "Nunito Sans", Arial, sans-serif;
    font-size: 11px;
    fill: var(--brand-red);
  }
</style>
</head>
<body>
<main class="battle-card">
  <h1 class="card-title">SEO Battle Card - Actual Competitor Matrix</h1>
  <div class="card-rule card-rule--top"></div>

  <svg class="matrix" width="1200" height="984" viewBox="0 0 1200 984" aria-label="Competitor matrix of Adword versus Organic share">
    <!-- grid -->
    <g class="grid" stroke="var(--grid)" stroke-width="1" fill="none">
      <line x1="215" y1="181" x2="847" y2="181"/>
      <line x1="847" y1="178" x2="847" y2="809"/>
      <line x1="527" y1="181" x2="527" y2="809"/>
      <line x1="215" y1="494" x2="847" y2="494"/>
    </g>

    <!-- axes -->
    <g class="axes" stroke="var(--axis)" stroke-width="2">
      <line x1="215" y1="181" x2="215" y2="809"/>
      <line x1="215" y1="809" x2="847" y2="809"/>
    </g>
    <g class="axis-ticks" fill="var(--axis)">
      <circle cx="215" cy="181" r="2.5"/><circle cx="215" cy="244" r="2.5"/>
      <circle cx="215" cy="307" r="2.5"/><circle cx="215" cy="370" r="2.5"/>
      <circle cx="215" cy="432" r="2.5"/><circle cx="215" cy="494" r="2.5"/>
      <circle cx="215" cy="558" r="2.5"/><circle cx="215" cy="621" r="2.5"/>
      <circle cx="215" cy="683" r="2.5"/><circle cx="215" cy="746" r="2.5"/>
      <circle cx="215" cy="809" r="2.5"/>
      <circle cx="278" cy="809" r="2.5"/><circle cx="340" cy="809" r="2.5"/>
      <circle cx="403" cy="809" r="2.5"/><circle cx="465" cy="809" r="2.5"/>
      <circle cx="527" cy="809" r="2.5"/><circle cx="590" cy="809" r="2.5"/>
      <circle cx="653" cy="809" r="2.5"/><circle cx="715" cy="809" r="2.5"/>
      <circle cx="778" cy="809" r="2.5"/>
    </g>

    <!-- axis labels -->
    <text class="axis-label" x="79" y="185">Adword</text>
    <text class="axis-label" x="878" y="813">Organic</text>

    <g class="tick-label" text-anchor="end">
      <text x="193" y="186">100%</text>
      <text x="193" y="249">90%</text>
      <text x="193" y="313">80%</text>
      <text x="193" y="375">70%</text>
      <text x="193" y="437">60%</text>
      <text x="193" y="502">50%</text>
      <text x="193" y="565">40%</text>
      <text x="193" y="627">30%</text>
      <text x="193" y="691">20%</text>
      <text x="193" y="753">10%</text>
      <text x="193" y="811">0%</text>
    </g>
    <g class="tick-label" text-anchor="middle">
      <text x="281" y="841">10%</text>
      <text x="345" y="841">20%</text>
      <text x="408" y="841">30%</text>
      <text x="469" y="841">40%</text>
      <text x="532" y="841">50%</text>
      <text x="598" y="841">60%</text>
      <text x="656" y="841">70%</text>
      <text x="719" y="841">80%</text>
      <text x="782" y="841">90%</text>
      <text x="844" y="841">100%</text>
    </g>

    <!-- legend -->
    <text class="legend-title" x="879" y="184">Competitor sites 1 to 7</text>
    <g class="legend">
      <circle cx="891" cy="214" r="12" fill="var(--site-1)"/>
      <circle cx="921" cy="214" r="11" fill="var(--site-2)"/>
      <circle cx="948" cy="214" r="10" fill="var(--site-3)"/>
      <circle cx="972" cy="214" r="8" fill="var(--site-4)"/>
      <circle cx="993" cy="214" r="8" fill="var(--site-5)"/>
      <circle cx="1015" cy="214" r="8" fill="var(--site-6)"/>
      <circle cx="1036" cy="214" r="8" fill="var(--site-7)"/>
    </g>

    <!-- competitor bubbles -->
    <g class="competitors">
      <circle cx="231" cy="494" r="20" fill="var(--site-1)"/>
      <circle cx="226" cy="621" r="13" fill="var(--site-2)"/>
      <circle cx="218" cy="672" r="13" fill="var(--site-3)"/>
      <circle cx="441" cy="809" r="15" fill="var(--site-2)"/>
      <circle cx="382" cy="809" r="10" fill="var(--site-6)"/>
      <circle cx="494" cy="809" r="10" fill="var(--site-5)"/>
      <circle cx="518" cy="691" r="12" fill="var(--site-7)"/>
    </g>

    <!-- own site -->
    <g class="own-site">
      <text class="own-site-label" x="565" y="585" text-anchor="middle">Your</text>
      <text class="own-site-label" x="565" y="599" text-anchor="middle">website</text>
      <line x1="565" y1="605" x2="565" y2="612" stroke="var(--brand-red)" stroke-width="1" stroke-dasharray="1.5 1.5"/>
      <circle cx="565" cy="636" r="24" fill="var(--brand-red)"/>
      <g stroke="#ffffff" stroke-width="2">
        <line x1="559" y1="636" x2="571" y2="636"/>
        <line x1="565" y1="630" x2="565" y2="642"/>
      </g>
    </g>
  </svg>

  <div class="card-rule card-rule--bottom"></div>
  <p class="card-footer">All images and data are property of Trevla Technology SA</p>
</main>
</body>
</html>
```